Business card design for Velvet Harbor

We need business cards designed for our new marketing consulting company, Velvet Harbor. Our services include marketing strategy, go-to-market and launch planning, growth strategy, and execution. We serve medical technology and health technology companies, from startups to well-established growth companies.

The business cards should feel professional, credible, reliable and trustworthy, and should instill confidence. Also bold, creative, and modern.

The design must use the Velvet Harbor logo.

The primary brand color is this orange: #FF5501
A secondary color that you can use is this gray: #282B2D
I would prefer only to use the orange and gray. But if you feel you really need an additional accent color (please use it very sparingly, as little as possible), you can use this blue for small accent purposes: #009FED

Attached are the logo files. The main logo is the one with a little bit of orange on the left and the rest is gray.

The business card should include the following:

Velvet Harbor logo
First name and last name
Title
Email address
Phone number and type (in whatever order looks best for the design
Website (the website does not need to be in the same block as the personal info)

For example:

Nessa Pryle
Founder & Principal
nessa@velvetharbor.com
+1.628.309.4156 mobile (can use "." or spaces in between blocks of numbers)
velvetharbor.com (somewhere on the card, it does not need to be with the personal info; and note that there is no "www." at the beginning)

Note that there will be no address listed on the business card.

Target Market(s)

Executives (CEO, head of marketing, head of sales) at medical technology and health technology companies, mostly in their 40s and older, well-educated, often with advanced degrees. They are strategic thinkers, responsible for budgets, and familiar with P&L. Their comfort with and trust in using outside consultants varies.

Industry/Entity Type

Medical technology and health technology companies.

Contact Information for Business Card

See project description

Font styles to use
Sans Serif

Requirements
Must have
• Logo and see Business card details section above.

```html
<!DOCTYPE html>
<html lang="en">
<head>
<meta charset="utf-8">
<title>Velvet Harbor — Business Card</title>
<link rel="stylesheet" href="https://fonts.googleapis.com/css2?family=Michroma&family=Arimo:wght@400&display=swap">
<style>
  :root {
    --stage: #3d3d3d;
    --orange: #ff5501;
    --gray: #282b2d;
    --white: #ffffff;
    --line: rgba(255,255,255,0.55);
  }
  * { box-sizing: border-box; margin: 0; padding: 0; }
  html, body {
    width: 1200px; height: 803px; overflow: hidden;
    background: var(--stage);
  }
  .stage {
    width: 1200px; height: 803px;
    display: flex; align-items: center; justify-content: center; gap: 60px;
  }
  .card {
    width: 520px; height: 297px;
    border-radius: 18px;
    position: relative;
    box-shadow: 0 14px 30px rgba(0,0,0,0.35);
  }
  .card-back { background: var(--orange); color: var(--white); }
  .card-front { background: var(--white); }

  .identity {
    position: absolute; left: 30px; top: 0; bottom: 0;
    width: 215px;
    display: flex; flex-direction: column; justify-content: center; align-items: flex-end;
    text-align: right;
  }
  .identity-name {
    font-family: "Michroma", sans-serif;
    font-size: 22px; line-height: 1.2; letter-spacing: 0.5px;
    white-space: nowrap;
  }
  .identity-title {
    font-family: "Arimo", sans-serif;
    font-size: 12px; margin-top: 4px;
  }
  .divider {
    position: absolute; left: 262px; top: 96px;
    width: 1px; height: 105px; background: var(--line);
  }
  .contact {
    position: absolute; left: 280px; top: 0; bottom: 0;
    display: flex; flex-direction: column; justify-content: center;
    font-family: "Arimo", sans-serif;
    font-size: 11.5px; line-height: 1.6;
  }
  .contact-row { display: flex; align-items: center; gap: 7px; white-space: nowrap; }
  .contact-icon { width: 10px; height: 10px; flex: none; }

  .brand {
    position: absolute; inset: 0;
    display: flex; align-items: center; justify-content: center; gap: 22px;
  }
  .brand-dot {
    width: 58px; height: 58px; border-radius: 50%;
    background: var(--orange); flex: none;
  }
  .brand-name {
    font-family: "Michroma", sans-serif;
    font-size: 30px; line-height: 1.15; letter-spacing: 9px;
    color: var(--gray);
  }
</style>
</head>
<body>
<main class="stage">
  <section class="card card-back" aria-label="Card back with contact details">
    <div class="identity">
      <p class="identity-name">Nessa Pryle</p>
      <p class="identity-title">President</p>
    </div>
    <div class="divider"></div>
    <div class="contact">
      <p class="contact-row">
        <svg class="contact-icon" viewBox="0 0 10 10" aria-hidden="true"><path d="M2 1 L4 3 L3 4.2 Q4.5 6 5.8 7 L7 6 L9 8 L7.8 9.2 Q4 8.5 0.8 2.2 Z" fill="#fff"/></svg>
        +1.628.309.4156
      </p>
      <p class="contact-row">
        <svg class="contact-icon" viewBox="0 0 10 10" aria-hidden="true"><rect x="2.5" y="0.5" width="5" height="9" rx="1" fill="none" stroke="#fff"/></svg>
        +1.628.309.7720
      </p>
      <p class="contact-row">
        <svg class="contact-icon" viewBox="0 0 10 10" aria-hidden="true"><rect x="0.5" y="2" width="9" height="6.5" fill="#fff"/><path d="M0.5 2 L5 5.5 L9.5 2" fill="none" stroke="#ff5501"/></svg>
        nessa@velvetharbor.com
      </p>
      <p class="contact-row">
        <svg class="contact-icon" viewBox="0 0 10 10" aria-hidden="true"><circle cx="5" cy="5" r="4.5" fill="#fff"/><path d="M0.5 5 H9.5 M5 0.5 Q2 5 5 9.5 M5 0.5 Q8 5 5 9.5" fill="none" stroke="#ff5501" stroke-width="0.8"/></svg>
        velvetharbor.com
      </p>
    </div>
  </section>

  <section class="card card-front" aria-label="Card front with company name">
    <div class="brand">
      <span class="brand-dot"></span>
      <p class="brand-name">VELVET<br>HARBOR</p>
    </div>
  </section>
</main>
</body>
</html>
```